Harborline Building Partners
Owner's Rep
Professional
Daniel Marsh
Long Beach Island New Jersey
dan@harborlnbuildingpartners.com
www.harborlnbuildingpartners.com
Your advocate for your construction needs
* New Construction * Remolding Projects * Maintenance and Service work * Off-season and pre-season inspections

```html
<!DOCTYPE html>
<html lang="en">
<head>
<meta charset="utf-8">
<title>Harborline Building Partners – Business Card</title>
<link rel="stylesheet" href="https://fonts.googleapis.com/css2?family=Cinzel:wght@500;600&family=Open+Sans:wght@400;600&display=swap">
<style>
  :root{
    --bg:#e9ebee;
    --navy:#0f2a4d;
    --navy-deep:#0a1d38;
    --sky:#29a9e0;
    --sky-light:#7fd0f5;
    --blue-top:#2f8fc9;
    --blue-bottom:#0d3563;
    --white:#ffffff;
    --ink-soft:#c9dcef;
  }
  *{box-sizing:border-box;margin:0;padding:0}
  html,body{width:1200px;height:901px;overflow:hidden;background:var(--bg)}
  body{position:relative;font-family:"Open Sans",sans-serif}

  .card{position:absolute;left:280px;width:640px;height:366px;border-radius:22px;overflow:hidden;
        box-shadow:0 14px 30px rgba(10,29,56,.25)}
  .card--front{top:44px;background:var(--navy)}
  .card--back{top:490px;background:linear-gradient(160deg,var(--blue-top) 0%,#1c5f98 45%,var(--blue-bottom) 100%)}

  /* front */
  .front-shape{position:absolute;inset:0}
  .contact-block{position:absolute;left:42px;top:56px;color:var(--white)}
  .person-name{font-family:"Cinzel",serif;font-weight:600;font-size:25px;letter-spacing:1px;color:var(--sky-light)}
  .person-role{font-size:14px;color:var(--ink-soft);margin-top:2px}
  .location{margin-top:34px;font-size:14px;line-height:1.45;color:var(--ink-soft)}
  .contact-list{list-style:none;margin-top:32px;font-size:13px;line-height:1.9;color:var(--white)}
  .contact-list li{display:flex;align-items:center;gap:9px}
  .contact-list svg{width:14px;height:14px;flex:none}

  .brand{position:absolute;display:flex;align-items:center;gap:12px}
  .brand-dot{width:18px;height:18px;border-radius:50%;flex:none}
  .brand-name{font-family:"Open Sans",sans-serif;font-weight:600;text-transform:uppercase;line-height:1.25;letter-spacing:1px}
  .brand--front{right:30px;top:230px}
  .brand--front .brand-dot{background:var(--sky)}
  .brand--front .brand-name{color:var(--navy);font-size:19px;width:220px}

  /* back */
  .back-glow{position:absolute;right:-120px;top:-140px;width:480px;height:480px;border-radius:50%;
             background:radial-gradient(circle,rgba(255,255,255,.16),rgba(255,255,255,0) 70%)}
  .brand--back{left:150px;top:72px}
  .brand--back .brand-dot{background:var(--white)}
  .brand--back .brand-name{color:var(--white);font-size:26px;width:380px}
  .brand-rule{position:absolute;left:150px;top:180px;width:340px;height:2px;background:var(--sky-light)}
  .services{position:absolute;left:40px;top:208px;display:grid;grid-template-columns:310px 250px;row-gap:16px;column-gap:20px;list-style:none}
  .services li{display:flex;align-items:center;gap:9px;color:var(--white);font-size:14px;white-space:nowrap}
  .services svg{width:18px;height:18px;flex:none}
</style>
</head>
<body>

<section class="card card--front" aria-label="Business card front">
  <svg class="front-shape" viewBox="0 0 640 366" preserveAspectRatio="none" aria-hidden="true">
    <path d="M640 0 L640 366 L305 366 C325 255 390 200 640 185 Z" fill="var(--white)"/>
    <path d="M305 366 C325 255 390 200 640 185" fill="none" stroke="var(--sky)" stroke-width="6"/>
  </svg>

  <div class="contact-block">
    <h1 class="person-name">DANIEL MARSH</h1>
    <p class="person-role">Owner's Rep</p>
    <p class="location">Marlow Point Island<br>Eastshore</p>
    <ul class="contact-list">
      <li><svg viewBox="0 0 16 16"><circle cx="8" cy="8" r="8" fill="var(--sky)"/><path d="M5 4.5l1.5-.5 1 2-1 .8a5 5 0 0 0 2.7 2.7l.8-1 2 1-.5 1.5c-3.5.3-6.8-3-6.5-6.5z" fill="#fff"/></svg>(609) 555-0142</li>
      <li><svg viewBox="0 0 16 16"><circle cx="8" cy="8" r="8" fill="var(--sky)"/><rect x="4" y="5" width="8" height="6" fill="none" stroke="#fff" stroke-width="1.2"/><path d="M4 5l4 3.5L12 5" fill="none" stroke="#fff" stroke-width="1.2"/></svg>dan@harborlnbuildingpartners.com</li>
      <li><svg viewBox="0 0 16 16"><circle cx="8" cy="8" r="8" fill="var(--sky)"/><circle cx="8" cy="8" r="4" fill="none" stroke="#fff" stroke-width="1.1"/><path d="M4 8h8M8 4c-2 2.5-2 5.5 0 8M8 4c2 2.5 2 5.5 0 8" fill="none" stroke="#fff" stroke-width="1"/></svg>www.harborlnbuildingpartners.com</li>
    </ul>
  </div>

  <div class="brand brand--front">
    <span class="brand-dot"></span>
    <span class="brand-name">Harborline Building Partners</span>
  </div>
</section>

<section class="card card--back" aria-label="Business card back">
  <div class="back-glow"></div>
  <div class="brand brand--back">
    <span class="brand-dot"></span>
    <span class="brand-name">Harborline Building Partners</span>
  </div>
  <div class="brand-rule"></div>
  <ul class="services">
    <li><svg viewBox="0 0 18 18"><circle cx="9" cy="9" r="8" fill="none" stroke="#fff" stroke-width="1.4"/><path d="M5.5 9.2l2.3 2.3 4.7-4.9" fill="none" stroke="#fff" stroke-width="1.6"/></svg>Remolding Projects</li>
    <li><svg viewBox="0 0 18 18"><circle cx="9" cy="9" r="8" fill="none" stroke="#fff" stroke-width="1.4"/><path d="M5.5 9.2l2.3 2.3 4.7-4.9" fill="none" stroke="#fff" stroke-width="1.6"/></svg>New Construction</li>
    <li><svg viewBox="0 0 18 18"><circle cx="9" cy="9" r="8" fill="none" stroke="#fff" stroke-width="1.4"/><path d="M5.5 9.2l2.3 2.3 4.7-4.9" fill="none" stroke="#fff" stroke-width="1.6"/></svg>Off-season and pre-season inspections</li>
    <li><svg viewBox="0 0 18 18"><circle cx="9" cy="9" r="8" fill="none" stroke="#fff" stroke-width="1.4"/><path d="M5.5 9.2l2.3 2.3 4.7-4.9" fill="none" stroke="#fff" stroke-width="1.6"/></svg>Maintenance and Service work</li>
  </ul>
</section>

</body>
</html>
```